New Business Card Design For Re-Branded Company (New Logo)

We recently switched our DBA and had a new logo designed. We now need new business cards made around our new logo. We would like to stick with the color scheme in our logo: White, Orange, and Blue. We want to see original bold designs that reflect our position in the solar energy sector but we prefer simple over complicated.

We are curious about vertical designs so if you can translate your design onto a vertical layout we would be open to look at it. We especially like a few designs we have seen on here that are vertical with a black or very dark gray background. They have our logo on one side and then the normal vertical business card on the other side.

I have included a screenshot of one of the samples we like, labeled sample.jpg and a file we were given as an example of our logo on a dark background.

At the same time we are satisfied to stay with what we have always had in a horizontal format. If it's not a lot of extra work for you, designs that are submitted in both horizontal and vertical formats will be greatly appreciated.

Please submit your original, bold, clean designs for consideration. Contact us with any questions or comments that may arise.

Thank you and Good Luck,

RT

```html
<!DOCTYPE html>
<html lang="en">
<head>
<meta charset="utf-8">
<title>Radiant Tide – Business Card</title>
<link rel="stylesheet" href="https://fonts.googleapis.com/css2?family=Montserrat:wght@700&family=Open+Sans:wght@400;600;700&display=swap">
<style>
  :root {
    --stage: #2b2b2d;
    --brand-blue: #1877c2;
    --brand-orange: #f07a1a;
    --paper: #ffffff;
    --shadow: rgba(0, 0, 0, 0.45);
  }
  * { box-sizing: border-box; margin: 0; padding: 0; }
  html, body { width: 1200px; height: 900px; overflow: hidden; }
  body {
    background: var(--stage);
    position: relative;
    font-family: "Open Sans", Arial, sans-serif;
  }
  .card {
    position: absolute;
    width: 560px;
    height: 320px;
    border-radius: 22px;
    overflow: hidden;
    box-shadow: 0 14px 30px var(--shadow);
  }

  /* Front */
  .card-front {
    left: 110px; top: 130px;
    background: var(--brand-blue);
    display: flex; flex-direction: column; align-items: center; justify-content: center;
    gap: 18px;
  }
  .front-mark {
    width: 96px; height: 96px;
    border: 7px solid var(--paper);
    border-radius: 50%;
  }
  .front-name {
    font-family: "Montserrat", Arial, sans-serif;
    font-weight: 700;
    font-size: 50px;
    letter-spacing: 1px;
    color: var(--paper);
  }

  /* Back */
  .card-back {
    left: 530px; top: 450px;
    background: var(--paper);
  }
  .back-band { position: absolute; inset: 0; width: 100%; height: 100%; }
  .back-logo {
    position: absolute; left: 40px; top: 26px;
    display: flex; flex-direction: column; align-items: flex-start; gap: 8px;
  }
  .back-mark {
    width: 48px; height: 48px;
    border: 5px solid var(--brand-orange);
    border-radius: 50%;
    margin-left: 40px;
  }
  .back-name {
    font-family: "Montserrat", Arial, sans-serif;
    font-weight: 700;
    font-size: 30px;
    line-height: 1.1;
    color: var(--brand-blue);
  }
  .corner-disc {
    position: absolute; right: 22px; top: 34px;
    width: 128px; height: 128px;
    border-radius: 50%;
    background: var(--paper);
    border: 8px solid var(--brand-orange);
  }
  .contact {
    position: absolute; left: 40px; bottom: 20px;
    color: var(--paper);
  }
  .contact-name { font-weight: 700; font-size: 20px; line-height: 1.2; letter-spacing: 0.5px; }
  .contact-role { font-weight: 600; font-size: 11px; letter-spacing: 1px; margin-bottom: 8px; }
  .contact-list { list-style: none; }
  .contact-item {
    display: flex; align-items: center; gap: 10px;
    font-size: 14px; line-height: 20px;
  }
  .contact-icon { width: 13px; height: 13px; fill: none; stroke: var(--paper); stroke-width: 1.8; }
</style>
</head>
<body>

  <section class="card card-front" aria-label="Card front">
    <span class="front-mark" aria-hidden="true"></span>
    <span class="front-name">RADIANT TIDE</span>
  </section>

  <section class="card card-back" aria-label="Card back">
    <svg class="back-band" viewBox="0 0 560 320" preserveAspectRatio="none" aria-hidden="true">
      <polygon points="0,185 560,85 560,320 0,320" fill="var(--brand-blue)"/>
    </svg>

    <div class="back-logo">
      <span class="back-mark" aria-hidden="true"></span>
      <span class="back-name">RADIANT TIDE</span>
    </div>

    <span class="corner-disc" aria-hidden="true"></span>

    <div class="contact">
      <p class="contact-name">MARCUS HALLOWELL</p>
      <p class="contact-role">DIRECTOR</p>
      <ul class="contact-list">
        <li class="contact-item">
          <svg class="contact-icon" viewBox="0 0 16 16" aria-hidden="true"><path d="M3 2l3 1 1 3-2 1a8 8 0 0 0 4 4l1-2 3 1 1 3-2 1C7 14 2 9 2 4z"/></svg>
          505 0419 2276
        </li>
        <li class="contact-item">
          <svg class="contact-icon" viewBox="0 0 16 16" aria-hidden="true"><rect x="2" y="4" width="12" height="9"/><path d="M2 4l6 5 6-5"/></svg>
          marcus@hallowell.com
        </li>
        <li class="contact-item">
          <svg class="contact-icon" viewBox="0 0 16 16" aria-hidden="true"><circle cx="8" cy="8" r="6"/><path d="M2 8h12M8 2c3 3 3 9 0 12M8 2c-3 3-3 9 0 12"/></svg>
          www.radianttide.com
        </li>
      </ul>
    </div>
  </section>

</body>
</html>
```